Brindlemark Services Ltd

I'd like to create a company letterhead for the attached logo in word format.

I'd like to emphasis the icon in large translucent state from the left corner and ensure that the letterhead colouring matches the colour palette of the current logo with a contrast so it's clear to see. I've attached a copy of our sister company page on the app for reference.

```html
<!DOCTYPE html>
<html lang="en">
<head>
<meta charset="utf-8">
<title>Brindlemark Services Ltd — Letterhead</title>
<link rel="stylesheet" href="https://fonts.googleapis.com/css2?family=Lato:wght@400;700&display=swap">
<style>
  :root {
    --teal: #00b9a3;
    --teal-faint: #e3f6f3;
    --ink: #3a3a3a;
    --paper: #ffffff;
    --backdrop: #e9ebea;
  }
  * { margin: 0; padding: 0; box-sizing: border-box; }
  html, body {
    width: 1061px; height: 1200px; overflow: hidden;
    background: var(--backdrop);
    font-family: "Lato", Arial, sans-serif;
  }
  .letterhead {
    position: absolute; left: 130px; top: 34px;
    width: 800px; height: 1132px;
    background: var(--paper);
    overflow: hidden;
    box-shadow: 0 2px 10px rgba(0,0,0,0.12);
  }
  .backdrop-art { position: absolute; inset: 0; }
  .brand {
    position: absolute; left: 545px; top: 68px; width: 190px;
    text-align: center; color: var(--teal);
  }
  .brand-dot {
    width: 58px; height: 58px; border-radius: 50%;
    background: var(--teal); margin: 0 auto 14px;
  }
  .brand-name { font-size: 36px; line-height: 1; letter-spacing: -0.5px; }
  .brand-sub { font-size: 9px; letter-spacing: 6px; margin-top: 7px; }
  .footer-rule {
    position: absolute; left: 64px; top: 965px; width: 675px;
    height: 1px; background: var(--teal);
  }
  .contact-list {
    position: absolute; left: 61px; top: 978px;
    list-style: none; font-size: 13px; color: var(--ink); line-height: 17.5px;
  }
  .contact-list li { display: flex; align-items: center; gap: 6px; }
  .contact-list svg { width: 12px; height: 12px; fill: var(--teal); flex: none; }
  .address {
    position: absolute; right: 61px; top: 977px;
    text-align: right; font-style: normal; font-size: 13px;
    color: var(--ink); line-height: 17.5px;
  }
  .address .company { color: var(--teal); }
  .web {
    position: absolute; right: 59px; top: 1092px;
    font-size: 13px; color: #fff;
  }
  .web strong { font-weight: 700; }
</style>
</head>
<body>
  <main class="letterhead">
    <svg class="backdrop-art" viewBox="0 0 800 1132" width="800" height="1132" aria-hidden="true">
      <defs>
        <radialGradient id="corner-glow" cx="150" cy="120" r="520" gradientUnits="userSpaceOnUse">
          <stop offset="0" stop-color="#e3f6f3"/>
          <stop offset="0.55" stop-color="#f1faf8"/>
          <stop offset="1" stop-color="#ffffff" stop-opacity="0"/>
        </radialGradient>
      </defs>
      <rect class="corner-glow" x="0" y="0" width="800" height="760" fill="url(#corner-glow)" role="img" aria-label="Soft translucent brand emblem glow from the top-left corner"/>
      <circle cx="150" cy="120" r="108" fill="#eaf8f5" opacity="0.8"/>
      <path class="footer-wave" fill="var(--teal)"
        d="M0 1035 C120 1100 220 1120 300 1117 C420 1113 560 1062 660 1062 C720 1062 770 1075 800 1087 V1132 H0 Z"/>
    </svg>

    <header class="brand">
      <div class="brand-dot"></div>
      <div class="brand-name">Brindlemark</div>
      <div class="brand-sub">SERVICES LTD</div>
    </header>

    <div class="footer-rule"></div>

    <ul class="contact-list">
      <li><svg viewBox="0 0 24 24"><path d="M6.6 10.8a15 15 0 0 0 6.6 6.6l2.2-2.2a1 1 0 0 1 1-.25 11.4 11.4 0 0 0 3.6.57 1 1 0 0 1 1 1V20a1 1 0 0 1-1 1A17 17 0 0 1 3 4a1 1 0 0 1 1-1h3.5a1 1 0 0 1 1 1c0 1.25.2 2.45.57 3.57a1 1 0 0 1-.25 1z"/></svg>(555) 014-2236</li>
      <li><svg viewBox="0 0 24 24"><path d="M6 2h12v5H6zM3 8h18a1 1 0 0 1 1 1v8h-4v5H6v-5H2V9a1 1 0 0 1 1-1zm5 8v4h8v-4z"/></svg>(555) 014-2237</li>
      <li><svg viewBox="0 0 24 24"><path d="M2 5h20v14H2zm2 2v.5l8 5 8-5V7z"/></svg>info@brindlemarkservices.com</li>
    </ul>

    <address class="address">
      <span class="company">Brindlemark Services Ltd</span><br>
      48 Alder Row<br>
      Hollisford, CT 06999
    </address>

    <p class="web">www.<strong>brindlemarkservices</strong>.com</p>
  </main>
</body>
</html>
```